Tobias Wrenfield - Cinematographer

NEED:
I'm looking for a sleek, professional, modern business card that will give give the recipient the impression that they can trust their production will go smoothly by hiring me. I will bring creativity and knowledge to their shoot, so that we can create powerful images.
I am looking for a card with a strong style and design ethos that could be expanded to a website and a full visual/graphic/design entity for me.
ABOUT ME:
I am a mid-twenties cinematographer, I work on music video, narrative short, commercial, and corporate projects. I blend the science and artistry of cameras and filmmaking to tell a story. I'm an artist, a technician, and a manager.
DESIGN:
I like sleek, simple design. Black, dark grays, white, dark navy, steel blues, I love cyan, but also cyan and red. I am not a fan of earthy tones. I generally prefer modern, san-serif fonts over serifs. My old logo was based on an aperture, a multi-blade device at the back of a lens that controls how much light passes through, but I made it with so many colors, that it doesn't necessarily lend itself to a specific color-scheme or design ethos. I liked that the aperture design provided a sense of the technical requirements of my job. I'm a fan of matte business cards, but am open to plenty of specialty print processes to make an outstanding card.
ATTACHED FILES:
My Old Rainbox Aperture Logo, plus a few designs I've tried playing around with, but am not tied to. I AM OPEN TO NEW DESIGNS, DO NOT FEEL TIED TO THIS.
**I've pulled my old logo down from the attached files, and instead attached other business cards I like, so as not to mislead you where I would like to go.
INFO:
Name: Tobias Wrenfield
Job: Cinematographer
Email: tkwrenfield@quillbox.example
Phone: 503.618.2907
Website: tobiaswrenfield.example
Updates
I'm adding some images of other cards that I like, and removing my old logo, since I'm looking for something new, and don't want that old logo to push anyone a certain direction.

```html
<!DOCTYPE html>
<html lang="en">
<head>
<meta charset="utf-8">
<title>Tobias Wrenfield – Cinematographer Business Card</title>
<link rel="stylesheet" href="https://fonts.googleapis.com/css2?family=Advent+Pro:wght@300;400&display=swap">
<style>
  :root {
    --backdrop: #6b6b6b;
    --card: #000000;
    --card-edge: #8a8a8a;
    --ink: #ffffff;
    --disc: #cfd0d2;
  }
  * { margin: 0; padding: 0; box-sizing: border-box; }
  html, body {
    width: 1200px;
    height: 406px;
    overflow: hidden;
    background: var(--backdrop);
  }
  .sheet {
    position: relative;
    width: 1200px;
    height: 406px;
    font-family: "Advent Pro", "Arial Narrow", sans-serif;
    color: var(--ink);
  }
  .card {
    position: absolute;
    top: 9px;
    height: 388px;
    background: var(--card);
    outline: 1px solid var(--card-edge);
  }
  .card--front { left: 9px; width: 580px; }
  .card--back { left: 598px; width: 592px; }

  .mark-disc {
    position: absolute;
    left: 188px;
    top: 93px;
  }
  .mark-name {
    position: absolute;
    left: 0;
    width: 100%;
    top: 318px;
    text-align: center;
    font-weight: 300;
    font-size: 24px;
    letter-spacing: 0.5px;
  }

  .identity {
    position: absolute;
    left: 0;
    top: 62px;
    width: 100%;
    text-align: center;
  }
  .identity__name {
    font-weight: 300;
    font-size: 66px;
    line-height: 1;
    white-space: nowrap;
  }
  .identity__rule {
    display: block;
    width: 405px;
    height: 2px;
    margin: 14px auto 0;
    background: var(--ink);
  }
  .identity__role {
    margin-top: 8px;
    font-weight: 400;
    font-size: 20px;
    letter-spacing: 0.3px;
  }

  .contact {
    position: absolute;
    left: 0;
    top: 302px;
    width: 100%;
    text-align: center;
    font-style: normal;
    font-weight: 400;
    font-size: 15px;
    line-height: 20px;
  }
</style>
</head>
<body>
<main class="sheet">
  <section class="card card--front" aria-label="Card front">
    <svg class="mark-disc" width="200" height="200" viewBox="0 0 200 200" aria-hidden="true">
      <circle cx="100" cy="100" r="100" fill="var(--disc)"/>
    </svg>
    <p class="mark-name">Tobias Wrenfield</p>
  </section>

  <section class="card card--back" aria-label="Card back">
    <header class="identity">
      <h1 class="identity__name">Tobias Wrenfield</h1>
      <span class="identity__rule"></span>
      <p class="identity__role">Cinematographer</p>
    </header>
    <address class="contact">
      <p>Email: tkwrenfield@quillbox.example</p>
      <p>Phone: 503.618.2907</p>
      <p>Website: tobiaswrenfield.example</p>
    </address>
  </section>
</main>
</body>
</html>
```